Flyer-Design
Sehr flexibel bei Änderungswünschen. Herzlichen Dank. Würde jederzeit wieder mit Ursula zusammenarbeiten.
Zielgruppe
Wir sind eine eine Praxis und unsere Zielgruppe sind Kunden. Es sollte einen Faltflyer geben, welcher Doppelseitig bedruckt wird.
Aufgabenstellung
Ich habe genaue Vorstellungen, wie dieser Flyer aussehen soll. Jedoch bin ich auch auf neue Ideen gespannt :). Wunschvorstellung wäre ein Falzflyer (siehe Bild Musterfyler). Des weiteren habe ich ein Word gemacht, mit dem gesamten Inhalt des Textes und wie der Flyer am Besten aufgebaut werden sollte. (siehe Flyer Tierversicherung).
Die beiden letzten Abschnitte (Tipp an unsere Kunden, Fazit) sollten ein wenig auffallen. Müssen auch nicht am Schluss sein.
Des weiteren wäre ich dankbar, wenn das CI/CD der Unternehmung berücksichtig wird. Bitte werfen Sie einen Blick auf die Webseite www.felbor-tieraerzte.ch. Ein Logo ist ebenfalls im Anhang. Bei Fragen bitte melden.
Ich freue mich auf Vorschläge.

```html
<!DOCTYPE html>
<html lang="de">
<head>
<meta charset="utf-8">
<title>Felbor Tierärzte – Tierversicherungen</title>
<link href="https://fonts.googleapis.com/css2?family=Fira+Sans:ital,wght@0,300;0,400;0,500;0,700;0,800;1,400&display=swap" rel="stylesheet">
<style>
  :root{
    --red:#d2123f;
    --grey:#a3a4a6;
    --text-grey:#6f7072;
    --white:#ffffff;
  }
  *{box-sizing:border-box;margin:0;padding:0}
  html,body{width:1200px;height:848px;overflow:hidden;background:var(--white)}
  body{font-family:"Fira Sans",sans-serif;color:var(--red);position:relative}
  .top-band{position:absolute;left:0;top:0;width:1200px;height:42px;background:var(--grey)}
  .top-band span{position:absolute;top:0;width:1px;height:42px;background:#b3b4b6}
  .panel{position:absolute;top:42px;width:400px;height:806px}
  .panel-intro{left:0}
  .panel-info{left:400px}
  .panel-cover{left:800px}

  .intro-text{position:absolute;left:51px;top:21px;width:350px;font-size:13.9px;line-height:18.9px;letter-spacing:-0.1px}
  .intro-text p{margin-bottom:18.6px}
  .tip-box{position:absolute;left:0;top:570px;width:400px;height:236px;background:var(--grey);color:var(--white)}
  .tip-box::before{content:"";position:absolute;left:0;top:0;width:400px;height:6px;
    background:repeating-linear-gradient(90deg,var(--white) 0 2px,transparent 2px 5px)}
  .tip-box h2{position:absolute;left:29px;top:22px;font-size:26.5px;font-weight:700;letter-spacing:-0.2px}
  .tip-box p{position:absolute;left:51px;top:70px;width:345px;font-style:italic;font-size:15.2px;line-height:20.5px;letter-spacing:-0.2px}

  .brand{font-weight:500;color:var(--red);letter-spacing:2px;text-transform:uppercase;line-height:1.05}
  .brand-small{position:absolute;left:180px;top:26px;font-size:22px}
  .brand-large{position:absolute;left:26px;top:22px;font-size:38px}

  .section-title{position:absolute;left:50px;font-size:30px;font-weight:400}
  .hours-title{top:100px}
  .day{position:absolute;left:82px;font-size:18px;font-weight:500}
  .time{position:absolute;left:134px;font-size:17px}
  .dots{position:absolute;left:40px;top:398px;display:flex;gap:12.7px}
  .dots span{width:15px;height:15px;border-radius:50%;background:var(--red);box-shadow:0 2px 0 #9c9d9f}
  .contact-title{top:463px}
  .contact-row{position:absolute;left:92px;display:flex;align-items:flex-start}
  .contact-row svg{width:24px;height:24px;margin-right:11px;flex:none;fill:none;stroke:var(--red);stroke-width:1.3}
  .contact-row span{font-size:18px;font-weight:300;color:var(--text-grey);line-height:24.5px}

  .cat-photo{position:absolute;left:0;top:124px;width:400px;height:515px;
    background:radial-gradient(ellipse at 55% 55%,#efeae4 0%,#d9cfc4 35%,#a48c74 62%,#4a3a2c 100%)}
  .cover-title{position:absolute;right:22px;top:660px;text-align:right;font-weight:700;font-size:27px;line-height:35px}
  .cover-sub{position:absolute;right:22px;top:738px;font-weight:700;font-size:19px}
</style>
</head>
<body>
  <div class="top-band"><span style="left:400px"></span><span style="left:800px"></span></div>

  <section class="panel panel-intro">
    <div class="intro-text">
      <p>Haustiere sind für viele von uns von grosser Bedeutung und sensible Weggefährten, mit denen sich lachen, reden und auch einmal weinen lässt. Neben den vielen Vorzügen, die ein eigenes Haustier mit sich bringen, können diese auch krank werden oder einen Unfall haben.</p>
      <p>Wenn eine Behandlung das geliebte Haustier retten kann, jedoch hohe Kosten für Medikamente, Behandlungen, Operationen oder Klinikaufenthalte auslöst, dann entstehen bei vielen Personen ernsthafte Sorgen und Belastungen,<br>denen allerdings vorgebeugt werden kann.</p>
      <p>Mit einem Abschluss einer Tierversicherung gegen Unfall und Krankheit können verschiedene Vorkehrungen getroffen werden,<br>um hohe Kosten im Ernstfall zu reduzieren.</p>
      <p>Daher ist es wichtig, dass man sich vorgängig über die Möglichkeiten einer Tierversicherung gegen Unfall und Krankheit informiert, um bestmöglich vorbereitet zu sein, sollte es dem treuen Begleiter einmal schlecht gehen.</p>
      <p>In diesem Flyer finden Sie alles von A-Z, was sie über Tierversicherungen gegen Unfall und Krankheit wissen müssen.</p>
    </div>
    <div class="tip-box">
      <h2>Tipp an unsere Kunden:</h2>
      <p>Wir empfehlen Ihnen die die Tierarztkosten der letzten Jahre zusammenzustellen und zu prüfen, ob sie von der gewählten Versicherung übernommen worden wären. Bei diesem Vergleich darf aber der Selbstbehalt nicht ausser Acht gelassen werden.</p>
    </div>
  </section>

  <section class="panel panel-info">
    <div class="brand brand-small">Felbor<br>Tierärzte</div>
    <h2 class="section-title hours-title">Öffnungszeiten</h2>
    <div class="day" style="top:148px">Montag - Freitag</div>
    <div class="time" style="top:190px">08.00 - 12.00 Uhr</div>
    <div class="time" style="top:228px">13.30 - 18.00 Uhr</div>
    <div class="day" style="top:271px">Samstag</div>
    <div class="time" style="top:308px">08.00 - 12.00 Uhr</div>
    <div class="dots"><span></span><span></span><span></span><span></span><span></span><span></span><span></span><span></span><span></span><span></span><span></span><span></span><span></span></div>
    <h2 class="section-title contact-title">Kontakt</h2>
    <div class="contact-row" style="top:516px">
      <svg viewBox="0 0 24 24"><rect x="3" y="5" width="18" height="12"/><path d="M3 5l9 7 9-7M1 19h22"/></svg>
      <span>info@felbor-tieraerzte.ch</span>
    </div>
    <div class="contact-row" style="top:557px">
      <svg viewBox="0 0 24 24"><path d="M5 3l4 1 1 4-2 2c1 3 3 5 6 6l2-2 4 1 1 4-2 2C10 21 3 14 3 5z"/></svg>
      <span>041 555 01 23</span>
    </div>
    <div class="contact-row" style="top:599px">
      <svg viewBox="0 0 24 24"><circle cx="11" cy="11" r="9"/><path d="M2 11h18M11 2c-4 5-4 13 0 18M11 2c4 5 4 13 0 18M4 6h14M4 16h14"/></svg>
      <span>www.felbor-tieraerzte.ch</span>
    </div>
    <div class="contact-row" style="top:642px">
      <svg viewBox="0 0 24 24"><path d="M2 12L12 3l10 9M5 10v11h14V10M10 21v-6h4v6"/></svg>
      <span>Felbor Tierärzte<br>Mattenweg 9<br>6000 Seeberg</span>
    </div>
  </section>

  <section class="panel panel-cover">
    <div class="brand brand-large">Felbor<br>Tierärzte</div>
    <div class="cat-photo" role="img" aria-label="Foto einer dreifarbigen Katze, die entspannt liegt"></div>
    <h1 class="cover-title">Tierversicherungen gegen<br>Unfall und Krankheit</h1>
    <div class="cover-sub">Fluch oder Segen?</div>
  </section>
</body>
</html>
```